Maple Cove Laser Dermal Studio needs an 8 page WP redesign

We need a colorful re-design for an 8 page Wordpress website. The current preliminary website is live. The home page URL is http://maplecovelaserdermalstudio.com The new logo is live on the website also. I would like a (re)design using the colors that are represented by the new logo file, and any additional complimentary colors. The information regarding the business can be found on the website already, so please review it for insight. The name of the business is "Maple Cove Laser Dermal Studio".

Target Market(s)

The targeted website viewer is an adult female between the ages of 30 and 75 who is interested in facial renewal, wart removal and scar removal. This website should inspire in the target viewer the benefits of laser facial renewal, wart removal and new scar removal. Potential website viewers are wanting and searching for improved skin health and appearance. The website must represent the essence of a professional spa business.

Industry/Entity Type

Business

Font styles to use
Sans Serif

Requirements
Must have
• - The phone number placed in a visible and high value widget area that allows mobile phone browser dialing.

```html
<!DOCTYPE html>
<html lang="en">
<head>
<meta charset="utf-8">
<title>Maple Cove Laser Dermal Studio</title>
<link href="https://fonts.googleapis.com/css2?family=Open+Sans:wght@400;600;700&family=Oswald:wght@400&family=Roboto:wght@300;400;500&display=swap" rel="stylesheet">
<style>
:root{
  --purple:#9a1a9e;
  --purple-dark:#7c1480;
  --nav:#2a2a2a;
  --ink:#333;
  --muted:#666;
  --line:#e4e4e4;
  --soft:#f7f7f7;
  --footer:#1f1f1f;
  --footer-bar:#181818;
  --white:#fff;
}
*{margin:0;padding:0;box-sizing:border-box}
html,body{width:672px;height:1200px;overflow:hidden;background:var(--white)}
body{position:relative;font-family:"Open Sans",Arial,sans-serif;color:var(--ink)}
.abs{position:absolute}
.hero{left:0;top:0;width:672px;height:366px;background:linear-gradient(90deg,#b9ac86 0%,#d9c7a8 25%,#e8cdb8 50%,#d8c49d 75%,#b8a878 100%)}
.hero-arrow{width:19px;height:19px;border-radius:50%;background:rgba(30,30,30,.8);top:193px}
.hero-title{left:0;width:672px;top:270px;text-align:center;font-family:"Oswald",sans-serif;font-size:32px;color:var(--white)}
.header-band{left:96px;top:0;width:480px;height:64px;background:rgba(235,230,222,.55)}
.call{left:111px;top:21px;width:21px;height:21px;border:1.5px solid var(--white);border-radius:50%}
.call-label{left:141px;top:20px;font-size:9.5px;font-style:italic;font-weight:700;color:var(--white)}
.call-number{left:141px;top:35px;font-size:8.5px;font-weight:600;color:#222}
.brand{left:236px;top:24px;width:200px;text-align:center;font-family:"Roboto",sans-serif;font-weight:500;font-size:12.5px;color:var(--purple-dark)}
.search{left:469px;top:25px;width:96px;height:18px;background:var(--white);border:1px solid #ddd;border-radius:2px;font-size:6.5px;color:#999;padding:5px 6px}
.nav{left:96px;top:64px;width:480px;height:35px;background:var(--nav);display:flex;align-items:center}
.nav-home{width:46px;height:35px;background:var(--purple);display:flex;align-items:center;justify-content:center}
.nav a{color:var(--white);font-family:"Roboto",sans-serif;font-size:7.5px;text-decoration:none;padding:0 0 0 12px}
.services{left:96px;top:334px;width:480px;height:110px;background:var(--white);border:1px solid var(--line)}
.service-img{top:336px;width:156px;height:103px}
.service-mid{left:256px;top:334px;width:160px;height:222px;background:var(--white);box-shadow:0 6px 10px rgba(0,0,0,.12)}
.service{top:456px;width:160px;text-align:center}
.service h3{font-family:"Roboto",sans-serif;font-weight:400;font-size:9px;letter-spacing:.4px;color:#444}
.service p{margin:13px auto 0;width:146px;font-size:6.6px;line-height:11.6px;color:#555}
.btn{display:inline-block;margin-top:11px;padding:5px 6px;border:1px solid var(--purple);border-radius:3px;font-family:"Roboto",sans-serif;font-size:7px;color:var(--purple)}
.welcome{left:96px;top:572px;font-family:"Roboto",sans-serif;font-weight:300;font-size:22px;color:var(--purple)}
.welcome-sub{left:96px;top:601px;font-family:"Roboto",sans-serif;font-size:12px;color:#444}
.welcome-img{left:96px;top:626px;width:143px;height:118px;background:linear-gradient(135deg,#d8c2a8,#efe4d8 50%,#bfb2a4)}
.welcome-head{left:252px;top:624px;width:160px;font-family:"Roboto",sans-serif;font-size:8.5px;line-height:12px;color:#333;letter-spacing:.2px}
.welcome-text{left:252px;top:655px;width:158px;font-size:6.5px;line-height:11.5px;color:#444}
.special{left:441px;top:578px;width:135px;height:166px;background:var(--soft);border:1px solid var(--line)}
.special-head{height:28px;background:var(--purple);color:var(--white);font-family:"Roboto",sans-serif;font-size:8.5px;text-align:center;line-height:28px}
.deal{height:23px;border-bottom:1px solid var(--line);font-size:6.8px;color:#555;text-align:center;line-height:23px}
.special-call{margin-top:19px;text-align:center;font-family:"Oswald",sans-serif;font-size:9px;line-height:15px;color:var(--purple)}
.posts-title{left:96px;top:771px;font-family:"Roboto",sans-serif;font-size:12px;color:#333}
.pager{top:776px;width:11px;height:11px;border:1px solid #ddd;border-radius:50%}
.posts-rule{left:96px;top:798px;width:480px;height:1px;background:var(--line)}
.post-img{top:815px;width:98px;height:93px}
.post{top:815px;width:116px}
.post h4{font-family:"Roboto",sans-serif;font-weight:400;font-size:8.5px;color:#333}
.post .date{margin-top:5px;font-family:"Roboto",sans-serif;font-size:7px;color:var(--purple)}
.post p{margin-top:5px;font-size:6.2px;line-height:11.5px;color:#666;text-align:justify}
.post .more{margin-top:6px;font-size:6.6px;color:#555}
.quote-band{left:0;top:942px;width:672px;height:108px;background:var(--soft)}
.quote-text{left:118px;top:969px;width:436px;text-align:center;font-size:6.6px;line-height:11.6px;color:#666}
.quote-mark{font-family:Georgia,serif;font-size:16px;font-weight:700;color:#555}
.quote-name{left:0;width:672px;top:1017px;text-align:center;font-family:"Roboto",sans-serif;font-weight:500;font-size:8.5px;color:#444}
.footer{left:0;top:1050px;width:672px;height:112px;background:var(--footer)}
.footer h5{font-family:"Roboto",sans-serif;font-weight:400;font-size:8.5px;color:#ccc;letter-spacing:.3px}
.footer-col{top:1069px;color:#aaa;font-size:6.6px;line-height:11.6px}
.footer-col ul{list-style:none;margin-top:9px}
.footer-col li{line-height:11.6px}
.news-input{display:inline-block;width:82px;height:17px;background:#2f2f2f;font-size:6.2px;color:#888;padding:4px 7px;vertical-align:middle}
.news-btn{display:inline-block;height:17px;padding:3px 7px;margin-left:4px;background:var(--purple);border-radius:2px;color:var(--white);font-size:7px;font-weight:600;vertical-align:middle}
.social li{display:flex;align-items:center;line-height:15.6px}
.dot{width:5px;height:5px;background:#aaa;border-radius:50%;margin-right:9px}
.footer-bar{left:0;top:1162px;width:672px;height:38px;background:var(--footer-bar);border-top:1px solid #2a2a2a;text-align:center;font-size:6.4px;color:#aaa;line-height:38px}
.footer-bar strong{color:var(--white);font-weight:600}
</style>
</head>
<body>

<div class="abs hero" role="img" aria-label="Spa photo of a smiling woman receiving a facial massage among yellow and white flowers"></div>
<div class="abs hero-arrow" style="left:30px"><svg width="19" height="19"><path d="M11 5 L7 9.5 L11 14" stroke="#fff" stroke-width="1.6" fill="none"/></svg></div>
<div class="abs hero-arrow" style="left:620px"><svg width="19" height="19"><path d="M8 5 L12 9.5 L8 14" stroke="#fff" stroke-width="1.6" fill="none"/></svg></div>
<div class="abs hero-title">Laser Skin Renewal</div>

<div class="abs header-band"></div>
<div class="abs call"><svg width="18" height="18" viewBox="0 0 18 18"><path d="M6 4.5c.6-.4 1.2 0 1.4.6l.6 1.4c.2.5 0 .9-.4 1.2l-.5.4c.5 1.1 1.4 2 2.5 2.5l.4-.5c.3-.4.8-.6 1.2-.4l1.4.6c.6.2 1 .8.6 1.4-.6 1-1.6 1.4-2.6 1-2.4-.9-4.1-2.6-5-5-.4-1 0-2 1-2.6z" fill="#fff"/></svg></div>
<div class="abs call-label">Call Us</div>
<div class="abs call-number"><a href="tel:+15550142290" style="color:inherit;text-decoration:none">+1 555 014 2290</a></div>
<div class="abs brand">Maple Cove Laser Dermal Studio</div>
<div class="abs search">Search
  <svg class="abs" style="right:7px;top:5px" width="8" height="8" viewBox="0 0 8 8"><circle cx="3.3" cy="3.3" r="2.3" stroke="#aaa" fill="none"/><path d="M5 5 L7 7" stroke="#aaa"/></svg>
</div>

<nav class="abs nav">
  <div class="nav-home"><svg width="14" height="12" viewBox="0 0 14 12"><path d="M7 0 L14 6 H12 V12 H8.5 V8 H5.5 V12 H2 V6 H0 Z" fill="#fff"/></svg></div>
  <a href="#" style="padding-left:13px">ABOUT</a>
  <a href="#">SKIN RENEWAL</a>
  <a href="#" style="padding-left:20px">SCAR REMOVAL</a>
  <a href="#" style="padding-left:29px">WART REMOVAL</a>
  <a href="#" style="padding-left:14px">YOUR VISIT</a>
  <a href="#" style="padding-left:18px">CONTACT</a>
  <a href="#" style="padding-left:23px">BLOG</a>
</nav>

<div class="abs services"></div>
<div class="abs service-mid"></div>
<div class="abs service-img" style="left:99px;background:linear-gradient(135deg,#e9e4ea,#f4eef0 50%,#e2d6dc)" role="img" aria-label="Woman with headband receiving a laser skin treatment"></div>
<div class="abs service-img" style="left:259px;background:linear-gradient(135deg,#c9a68e,#b88f78 50%,#a77f68)" role="img" aria-label="Close view of an eye and brow area with a scar"></div>
<div class="abs service-img" style="left:419px;background:linear-gradient(135deg,#d89a86,#c9857a 50%,#b87468)" role="img" aria-label="Close view of a wart on the palm of a hand"></div>

<div class="abs service" style="left:96px"><h3>SKIN RENEWAL</h3><p>Lorem ipsum dolor sit amet, consectetur adipisicing elit, sed do eiusmod tempor didunt labore et dolore magna aliqua.</p><span class="btn">READ MORE</span></div>
<div class="abs service" style="left:256px"><h3>SCAR REMOVAL</h3><p>Lorem ipsum dolor sit amet, consectetur adipisicing elit, sed do eiusmod tempor didunt labore et dolore magna aliqua.</p><span class="btn">READ MORE</span></div>
<div class="abs service" style="left:416px"><h3>WART REMOVAL</h3><p>Lorem ipsum dolor sit amet, consectetur adipisicing elit, sed do eiusmod tempor didunt labore et dolore magna aliqua.</p><span class="btn">READ MORE</span></div>

<div class="abs welcome">Welcome To</div>
<div class="abs welcome-sub">Maple Cove Laser Dermal Studio</div>
<div class="abs welcome-img" role="img" aria-label="Client relaxing during a facial treatment in the studio"></div>
<div class="abs welcome-head">HAVE YOU CONSIDERED LASER SKIN RENEWAL THERAPY?</div>
<div class="abs welcome-text">You will truly love laser skin renewal if your skin is showing signs of premature aging or the skin has sustained sun damage. Conditions such as excessive redness due to sun exposure or fine lines will be concerns of the past. In fact, laser skin therapy is a unique and innovative way to enjoy youthful and healthy skin without resorting to painful and inconvenient surgery.</div>

<div class="abs special">
  <div class="special-head">New Years Resolution Special!</div>
  <div class="deal">SINGLE SESSION DEAL - $199</div>
  <div class="deal">SESSIONS PACKAGE DEAL - $549</div>
  <div class="deal">SESSIONS PACKAGE DEAL - $899</div>
  <div class="special-call"><a href="tel:5550193388" style="color:inherit;text-decoration:none">Call 555-019-3388 to Schedule<br>Your Convenient Appointment.</a></div>
</div>

<div class="abs posts-title">Recent Posts</div>
<div class="abs pager" style="left:551px"><svg width="9" height="9"><path d="M5 2.5 L3 4.5 L5 6.5" stroke="#888" fill="none"/></svg></div>
<div class="abs pager" style="left:565px"><svg width="9" height="9"><path d="M4 2.5 L6 4.5 L4 6.5" stroke="#888" fill="none"/></svg></div>
<div class="abs posts-rule"></div>

<div class="abs post-img" style="left:96px;background:linear-gradient(90deg,#cbb79a,#e6cdb6 50%,#d9cf6a)" role="img" aria-label="Smiling woman during a relaxing facial with yellow flowers"></div>
<div class="abs post" style="left:206px"><h4>Lorem ipsum dolor sit amet</h4><div class="date">Dec 31, 2014</div><p>Lorem ipsum dolor sit amet, consectetuer adipiscing elit, sed diam nonummy nibh euismod tincidunt ut laoreet dolore Lorem ipsum dolor sit amet, consectetuer</p><div class="more">Read More +</div></div>
<div class="abs post-img" style="left:345px;background:linear-gradient(90deg,#e9ddd2,#efe2d4 50%,#b9d08a)" role="img" aria-label="Woman with glowing skin smiling softly outdoors"></div>
<div class="abs post" style="left:454px"><h4>Lorem ipsum dolor sit amet</h4><div class="date">Dec 31, 2014</div><p>Lorem ipsum dolor sit amet, consectetuer adipiscing elit, sed diam nonummy nibh euismod tincidunt ut laoreet dolore Lorem ipsum dolor sit amet, consectetuer</p><div class="more">Read More +</div></div>

<div class="abs quote-band"></div>
<div class="abs quote-mark" style="left:96px;top:958px">&ldquo;</div>
<div class="abs quote-text">Lorem ipsum dolor sit amet, ea doming epicuri iudicabit nam, te usu virtute placerat. Purto brute disputando cu est, eam dicam soluta ei. Vel dicam vivendo accusata ei, cum ne periculis molestiae pri. Lorem ipsum dolor sit amet, ea doming epicuri iudicabit nam. Lorem ipsum dolor sit amet, ea doming epicuri &nbsp; Lorem ipsum dolor sit amet, ea doming epicuri iudicabit nam, te usu virtute placerat.</div>
<div class="abs quote-mark" style="left:566px;top:990px">&rdquo;</div>
<div class="abs quote-name">CLAIRE MORROW</div>

<footer class="abs footer"></footer>
<div class="abs footer-col" style="left:96px;width:126px"><h5>WHO WE ARE</h5><p style="margin-top:9px">Laser skin therapy is a non-invasive procedure that is extremely safe and effective. Above all, it is discrete and you never have to worry about family, friends and acquaintances, finding</p></div>
<div class="abs footer-col" style="left:249px"><h5>INFORMATION</h5><ul><li>Skin Renewal</li><li>Scar Removal</li><li>Wart Removal</li><li>Your Visit</li><li>Contact Us</li></ul></div>
<div class="abs footer-col" style="left:360px;width:140px"><h5>NEWSLETTER SIGNUP</h5><p style="margin-top:9px">Sign up to Our Newsletter &amp; get attractive Offers by subscribing to our newsletters.</p><div style="margin-top:6px"><span class="news-input">Enter Your Email</span><span class="news-btn">subscribe</span></div></div>
<div class="abs footer-col social" style="left:520px"><h5>SOCIAL MEDIA</h5><ul style="margin-top:7px"><li><span class="dot"></span>Friend Page</li><li><span class="dot"></span>Short Posts</li><li><span class="dot"></span>Circle Share</li><li><span class="dot"></span>Video Channel</li></ul></div>
<div class="abs footer-bar">&copy;2013 - 2014 &nbsp;<strong>MAPLE COVE LASER DERMAL STUDIO</strong>. All Rights Reserved.</div>

</body>
</html>
```